Geschäftspapiere für Hotel
Zielgruppe
Wir das 'GASTHAUS am Lindenbrunn', Hoher Birkenpfad 17, 48613 Lindenfeld, Tel.: 04817/53200 sind ein Hotel mit 11 Zimmern, Restaurant & 2 Doppelkegelbahnen. Wir bieten eine gutbürgerliche dutsche Küche.
Aufgabenstellung
Bitte nachtsehende 'alte Logo' so ändern wie in der Anlage. Habe ich grob skizziert.
Soll Quasi ein darunter hängendes Schild darstellen.

```html
<!DOCTYPE html>
<html lang="de">
<head>
<meta charset="utf-8">
<title>Briefbogen – GASTHAUS am Lindenbrunn</title>
<link href="https://fonts.googleapis.com/css2?family=Arimo&family=Fira+Sans:wght@400;500&display=swap" rel="stylesheet">
<style>
  :root {
    --brand-red: #a32414;
    --ink: #111111;
    --fold-mark: #c98a82;
    --paper: #ffffff;
  }
  html, body { margin: 0; padding: 0; overflow: hidden; background: var(--paper); }
  .letterhead {
    position: relative;
    width: 848px; height: 1200px;
    background: var(--paper);
    overflow: hidden;
    color: var(--ink);
    font-family: "Arimo", Arial, sans-serif;
  }
  .brand-name {
    position: absolute; left: 0; right: 0; top: 78px;
    text-align: center;
    font-family: "Fira Sans", sans-serif;
    font-weight: 500; font-size: 28px; letter-spacing: 0.5px;
    color: var(--brand-red);
  }
  .sender-line {
    position: absolute; left: 101px; top: 209px;
    font-family: "Fira Sans", sans-serif; font-size: 8.6px; white-space: nowrap;
  }
  .sender-line .name { color: var(--brand-red); }
  .sender-line .sep { color: var(--brand-red); margin: 0 3px; }
  .recipient {
    position: absolute; left: 101px; top: 229px;
    font-size: 15.5px; line-height: 20px;
  }
  .recipient .city { margin-top: 20px; }
  .fold-mark {
    position: absolute; left: 0; width: 40px; height: 0;
    border-top: 1px solid var(--fold-mark);
  }
  .subject, .body p, .closing {
    position: absolute; left: 101px; margin: 0;
    font-size: 15.5px; line-height: 21.4px; white-space: nowrap;
  }
  .subject { top: 431px; }
  .body p:nth-child(1) { top: 474px; }
  .body p:nth-child(2) { top: 602px; }
  .body p:nth-child(3) { top: 709px; }
  .closing { top: 880px; }
  .footer {
    position: absolute; top: 1119px; left: 0; right: 0;
    font-family: "Fira Sans", sans-serif; font-size: 9.6px; line-height: 17px;
  }
  .footer-col { position: absolute; top: 0; white-space: nowrap; }
  .footer-col .name { color: var(--brand-red); }
  .footer-col.address { left: 101px; }
  .footer-col.contact { left: 268px; }
  .footer-col.bank { left: 472px; }
  .footer-col.tax { left: 677px; }
  .contact-row { display: flex; align-items: center; gap: 8px; }
  .contact-row svg { width: 10px; height: 10px; flex: none; }
  .bottom-band { position: absolute; left: 0; bottom: 0; width: 848px; height: 14px; }
</style>
</head>
<body>
<div class="letterhead">
  <div class="brand-name">GASTHAUS am Lindenbrunn</div>

  <div class="sender-line">
    <span class="name">GASTHAUS am Lindenbrunn</span><span class="sep">|</span>Hoher Birkenpfad 17<span class="sep">|</span>48613 Lindenfeld
  </div>

  <div class="recipient">
    <div>Herrn</div>
    <div>Max Mustermann</div>
    <div>Musterstraße 00</div>
    <div class="city">01234 Musterstadt</div>
  </div>

  <div class="fold-mark" style="top:424px"></div>
  <div class="fold-mark" style="top:599px"></div>
  <div class="fold-mark" style="top:848px"></div>

  <p class="subject">Dies ist eine Betreffzeile</p>

  <div class="body">
    <p>Sehr geehrter Herr Mustermann, jeder Setzer hat für diesen Zweck immer etwas Blindtext<br>parat. Blindtext ist im Umfang von einigen tausend Anschlägen, der für die »äußerliche«<br>Gestaltung einer Publikation verwendet und dessen Inhalt unwichtig ist. Man setzt ihn oft zum<br>Beispiel in verschiedenen Schriften und Schriftgrößen, um anderen zu zeigen, wie eine<br>bestimmte Schrift wirkt.</p>
    <p>Oder man montiert auch komplette ganze Seiten mit sinnlosen Streifen von Blindtext, um das<br>spätere Aussehen der Seiten zu simulieren. Blindtext wird allerdings oft nur für die Teile einer<br>Seite verwendet, die in so kleiner Schrift gesetzt werden, dass sie beim »Überfliegen«<br>ungelesen bleiben.</p>
    <p>Jeder Setzer hat für diesen Zweck immer etwas Blindtext parat. Blindtext ist Umfang von<br>einigen tausend Anschlägen, der für die »äußerliche« Gestaltung einer Publikation verwendet<br>und dessen Inhalt unwichtig ist.</p>
  </div>

  <p class="closing">Mit freundlichen Grüßen</p>

  <footer class="footer">
    <div class="footer-col address">
      <div class="name">GASTHAUS am Lindenbrunn</div>
      <div>Hoher Birkenpfad 17</div>
      <div>48613 Lindenfeld</div>
    </div>
    <div class="footer-col contact">
      <div class="contact-row">
        <svg viewBox="0 0 10 10" fill="none" stroke="var(--brand-red)" stroke-width="1"><path d="M2 8.5 C1 7.5 1 5 3.5 2.5 S7.5 1 8.5 2 L7 3.5 L6 2.8 C5 3.5 3.5 5 2.8 6 L3.5 7 Z"/></svg>
        <span>04817 53200</span>
      </div>
      <div class="contact-row">
        <svg viewBox="0 0 10 10" fill="none" stroke="var(--brand-red)" stroke-width="1"><rect x="0.8" y="2" width="8.4" height="6"/><path d="M0.8 2 L5 5.5 L9.2 2 M0.8 8 L4 5 M9.2 8 L6 5"/></svg>
        <span>anfrage@gasthaus-lindenbrunn.de</span>
      </div>
      <div class="contact-row">
        <svg viewBox="0 0 10 10" fill="none" stroke="var(--brand-red)" stroke-width="0.9"><circle cx="5" cy="5" r="4.2"/><ellipse cx="5" cy="5" rx="1.8" ry="4.2"/><path d="M0.8 5 H9.2 M1.5 3 H8.5 M1.5 7 H8.5"/></svg>
        <span>www.gasthaus-lindenbrunn.de</span>
      </div>
    </div>
    <div class="footer-col bank">
      <div>Kreissparkasse Lippetal</div>
      <div>IBAN: DE27 4806 0250 0417 5523 08</div>
      <div>BIC: KSLIDE3LXXX</div>
    </div>
    <div class="footer-col tax">
      <div>Finanzamt Lippetal</div>
      <div>Steuer-Nr.: 318/6721/4093</div>
      <div>USt-IdNr.: DE284716302</div>
    </div>
  </footer>

  <svg class="bottom-band" viewBox="0 0 848 14" preserveAspectRatio="none">
    <path d="M0 14 Q424 -6 848 14 Z" fill="var(--brand-red)"/>
  </svg>
</div>
</body>
</html>
```